Web Design Project for a new website

We need a web design for a new proposed social media site ,intially to judge market response, this would be a basic site 4 pages with a register page for visitors to register with email and possibly start their own profile page with a template that would be on the site.
the domain is zenthra.net with the tagline dream climb reach zenthra ,,it has 2 aa in zenthra ,the main function and the message we would like to convey is that if you aspire to achieve your goals,aim in life ,change your life ,the site will recognize and reward you with a status rank more like a life rank,example is brivane 1000 most influential people,this would allow you to network with other likeminded people who register on site and progress of your goal could be monitored via your profile page.
There are 4 categories of how to become world zenthra
Star,Hero,Leader,Icon
And one category Q-7 which is a open forum on the science of success to which people registered can contribute and source info.
The design has to communicate the message of the site in a proffessional modern way with distinct colours and and logo that can be visually striking .

deadline is friday the 5th please submit your designs

Please submit designs as last day of deadline 5th august.

Reason: some designers have asked for extra time so obliging but cant extend any further so please submit designs by deadline .

Reason: 1 designer has asked for days extension.

12 to 80 all levels

Media

• see attached file for logo and design of zenthra the file can be changed or formatted or if be your own individual design on the same theme ,the main web logo of zenthra would also be the logo with a different colour identity fo categories STAR,HERO,LEADER,ICON ,Q-7
• zenthra.net should have the tagline dream,climb,reach zenthra
zenthra.net
dream,climb,reach zenthra,
the logo should indicate being world zenthra,a globe as per file image.some background messages like aspire,achive,be a world leader,can be used as background.

```html
<!DOCTYPE html>
<html lang="en">
<head>
<meta charset="utf-8">
<title>zenthra – Members Login</title>
<link rel="stylesheet" href="https://fonts.googleapis.com/css2?family=Open+Sans:ital,wght@0,400;0,600;1,400;1,700&display=swap">
<style>
  :root{
    --sky-deep:#2fa6e6;
    --sky-mid:#7fd3f2;
    --sky-pale:#d8f2fb;
    --white:#ffffff;
    --brand-ink:#1a6f10;
    --tagline-ink:#2c4a6e;
    --band-green-dark:#137a06;
    --band-green:#1c9c06;
    --panel-top:#ffffff;
    --panel-bottom:#f1f1f1;
    --panel-edge:#e2e2e2;
    --field-border:#d6d6d6;
    --field-text:#7a7a7a;
    --link-text:#888888;
    --lock-green:#5cc41c;
    --lock-green-dark:#2f9a0c;
    --figure-tone:#e6e6e6;
    --figure-accent:#e8531c;
  }
  *{box-sizing:border-box;margin:0;padding:0}
  html,body{width:1200px;height:873px;overflow:hidden;background:var(--white)}
  body{position:relative;font-family:"Open Sans",Arial,sans-serif}

  .sky-scene{
    position:absolute;left:0;top:0;width:1200px;height:470px;
    background:
      radial-gradient(ellipse 260px 140px at 80px 250px,rgba(255,255,255,.85),transparent 70%),
      radial-gradient(ellipse 260px 140px at 1120px 250px,rgba(255,255,255,.85),transparent 70%),
      linear-gradient(180deg,var(--sky-deep) 0%,var(--sky-mid) 38%,var(--sky-pale) 70%,var(--white) 100%);
  }

  .brand{
    position:absolute;left:0;top:160px;width:1200px;text-align:center;
  }
  .brand-name{
    font-weight:600;font-size:76px;line-height:1;letter-spacing:1px;
    color:var(--brand-ink);
  }
  .brand-tagline{
    margin-top:20px;font-weight:400;font-size:20px;
    letter-spacing:1px;color:var(--tagline-ink);
  }

  .login-panel{
    position:absolute;left:314px;top:337px;width:562px;height:268px;
    background:linear-gradient(180deg,var(--panel-top) 40%,var(--panel-bottom) 100%);
    border:1px solid var(--panel-edge);
    box-shadow:0 18px 16px -12px rgba(0,0,0,.35);
  }
  .login-band{
    position:absolute;left:300px;top:360px;width:591px;height:45px;
    background:linear-gradient(90deg,var(--band-green-dark),var(--band-green) 60%);
  }
  .login-band::before,.login-band::after{
    content:"";position:absolute;top:-14px;border-bottom:14px solid var(--band-green-dark);
  }
  .login-band::before{left:0;border-left:14px solid transparent}
  .login-band::after{right:0;border-right:14px solid transparent;border-bottom-color:var(--band-green)}
  .login-title{
    position:absolute;left:453px;top:367px;
    font-style:italic;font-weight:700;font-size:22px;letter-spacing:1.6px;color:var(--white);
  }
  .support-figure{
    position:absolute;left:332px;top:308px;width:112px;height:112px;border-radius:10px;
    background:linear-gradient(135deg,var(--figure-tone) 55%,var(--figure-accent) 100%);
  }

  .login-field{
    position:absolute;left:339px;width:384px;height:43px;border-radius:22px;
    border:2px solid var(--field-border);background:var(--white);
    box-shadow:inset 0 3px 4px rgba(0,0,0,.08);
    font-family:inherit;font-size:14.5px;color:var(--field-text);padding-left:26px;
  }
  .login-field::placeholder{color:var(--field-text)}
  .field-user{top:435px}
  .field-pass{top:493px}

  .login-button{
    position:absolute;left:752px;top:440px;width:108px;height:100px;border:0;background:none;cursor:pointer;
  }

  .login-links{
    position:absolute;left:367px;top:566px;font-style:italic;font-size:14px;color:var(--link-text);
  }
  .login-links a{color:var(--link-text);text-decoration:none}
  .login-links .divider{font-style:normal;margin:0 14px 0 30px}
</style>
</head>
<body>
  <div class="sky-scene" role="img" aria-label="Bright blue sky with light rays and soft white clouds"></div>

  <header class="brand">
    <div class="brand-name">zenthra</div>
    <p class="brand-tagline">dream, climb, reach zenthra</p>
  </header>

  <section class="login-panel" aria-label="Members login"></section>
  <div class="login-band"></div>
  <div class="support-figure" role="img" aria-label="Support figure with headset working at a laptop"></div>
  <h1 class="login-title">Members Login Area</h1>

  <form>
    <input class="login-field field-user" type="text" placeholder="Enter your User Name/ ID">
    <input class="login-field field-pass" type="password" placeholder="Enter your Password">
    <button class="login-button" type="submit" aria-label="Log in">
      <svg width="108" height="100" viewBox="0 0 108 100">
        <ellipse cx="56" cy="82" rx="46" ry="12" fill="rgba(0,0,0,.25)"/>
        <circle cx="52" cy="48" r="48" fill="#ffffff" stroke="#e4e4e4" stroke-width="2"/>
        <circle cx="52" cy="46" r="40" fill="var(--lock-green)"/>
        <circle cx="52" cy="46" r="40" fill="none" stroke="var(--lock-green-dark)" stroke-width="3"/>
        <path d="M41 42v-8a11 11 0 0 1 22 0v8" fill="none" stroke="#e9f9dc" stroke-width="5"/>
        <rect x="36" y="41" width="32" height="25" rx="3" fill="#e9f9dc"/>
        <rect x="50" y="48" width="4" height="10" rx="2" fill="var(--lock-green-dark)"/>
      </svg>
    </button>
  </form>

  <nav class="login-links">
    <a href="#">Forgot Password??</a><span class="divider">|</span><a href="#">New User Register Now</a>
  </nav>
</body>
</html>
```